KORVAN TECH LTD

Advertisement to get more schools:
use website https://www.korvan-tech.co.uk for logos etc.
ICT Service Level Agreements for as little as £2000 per year
Unlimited Remote, phone and email support
Unlimited Call outs included
90% fix time within 30 minutes of ticket submission
Extra support during Quadrel inspections
GDPR service included

```html
<!DOCTYPE html>
<html lang="en">
<head>
<meta charset="utf-8">
<title>KORVAN TECH LTD – ICT Service Level Agreements</title>
<link href="https://fonts.googleapis.com/css2?family=Montserrat:wght@400;500;700;800&display=swap" rel="stylesheet">
<style>
  :root {
    --brand-blue: #1f6fc1;
    --brand-blue-deep: #14508f;
    --accent-orange: #f26a21;
    --panel-light: #f5f5f5;
    --panel-white: #ffffff;
    --body-grey: #5a5a5a;
    --envelope-yellow: #f4d27a;
    --envelope-blue: #a9d1ee;
    --backpack-khaki: #cfc8a6;
    --book-tan: #e9bd8c;
  }
  * { box-sizing: border-box; margin: 0; padding: 0; }
  html, body { width: 1200px; height: 700px; overflow: hidden; background: var(--panel-white); }
  .advert {
    position: relative;
    width: 1200px;
    height: 700px;
    overflow: hidden;
    font-family: "Montserrat", Arial, sans-serif;
    background: linear-gradient(180deg, var(--panel-white) 0%, var(--panel-light) 60%, var(--panel-white) 100%);
  }
  .hero {
    position: absolute; left: 0; top: 0; width: 1200px; height: 226px;
    background: linear-gradient(100deg, var(--brand-blue-deep) 0%, var(--brand-blue) 45%, #3d8ad6 75%, var(--brand-blue-deep) 100%);
  }
  .hero-title {
    position: absolute; left: 0; top: 44px; width: 100%;
    text-align: center; color: #fff; font-weight: 700; font-size: 60px; letter-spacing: 0.5px;
  }
  .hero-subtitle {
    position: absolute; left: 0; top: 128px; width: 100%;
    text-align: center; color: #fff; font-weight: 500; font-size: 26px;
  }
  .price-tag {
    display: inline-block; background: var(--accent-orange); color: #fff;
    font-weight: 800; font-size: 32px; padding: 0 12px; border-radius: 10px;
    margin-left: 6px; vertical-align: -2px; line-height: 44px;
  }
  .accent-band {
    position: absolute; left: 0; top: 232px; width: 1200px; height: 12px;
    background: var(--accent-orange);
  }
  .benefits {
    position: absolute; left: 0; top: 324px; width: 100%;
    list-style: none; text-align: center; color: var(--body-grey);
    font-size: 26px; font-weight: 500; line-height: 48px;
  }
  .benefits .highlight { color: var(--accent-orange); }
  .illustration { position: absolute; border-radius: 14px; }
  .illustration--envelope { left: 92px; top: 306px; width: 104px; height: 80px; background: var(--envelope-yellow); transform: rotate(-12deg); }
  .illustration--open-envelope { left: 82px; top: 490px; width: 120px; height: 150px; background: var(--envelope-blue); transform: rotate(-6deg); }
  .illustration--backpack { left: 1008px; top: 288px; width: 92px; height: 124px; background: var(--backpack-khaki); border-radius: 24px; }
  .illustration--book { left: 980px; top: 492px; width: 150px; height: 156px; background: var(--book-tan); transform: rotate(4deg); }
  .company {
    position: absolute; left: 0; top: 614px; width: 100%;
    text-align: center; color: var(--body-grey);
    font-weight: 500; font-size: 24px; letter-spacing: 0.5px;
  }
</style>
</head>
<body>
  <main class="advert">
    <header class="hero" role="img" aria-label="Photo of pupils using ICT equipment in a classroom, tinted blue"></header>
    <h1 class="hero-title">ICT Service Level Agreements</h1>
    <p class="hero-subtitle">ICT Service Level Agreements for as little as <span class="price-tag">£ 2000</span> per year</p>
    <div class="accent-band"></div>

    <div class="illustration illustration--envelope" role="img" aria-label="Illustration of a closed yellow envelope"></div>
    <div class="illustration illustration--open-envelope" role="img" aria-label="Illustration of an open envelope with a letter"></div>
    <div class="illustration illustration--backpack" role="img" aria-label="Illustration of a school backpack"></div>
    <div class="illustration illustration--book" role="img" aria-label="Illustration of an open notebook with a pencil"></div>

    <ul class="benefits">
      <li>Unlimited Remote, phone and email support</li>
      <li>Unlimited Call outs included</li>
      <li><span class="highlight">90%</span> fix time within <span class="highlight">30 minutes</span> of ticket submission</li>
      <li>Extra support during Quadrel inspections</li>
      <li>GDPR service included</li>
    </ul>

    <footer class="company">KORVAN TECH LTD</footer>
  </main>
</body>
</html>
```